Custom sign and personalization company needing a website

UPDATED - Need a website to showcase our custom products. We use CNC, Laser and sublimation for our products. Because all our work is custom we would like it easy for clients to reach out to us via a contact page. A similar website would be https://brindlewoodcraft.com/. Of course, the subpages under shop and services will be different. There will not be a need for a custom order form. This website is a little basic. Looking for one that really grabs attention.

Thank You

Target Market(s)

Those looking for custom items.

Industry/Entity Type

Custom items

Coding

Coded - Design and coding required

Number of Pages Required

5+ page

Requirements
Must have
• Carousel on the main page to show different . Photographs of recent work on the bottom of the home page.
Nice to have
• Incorporate the colors of the logo.

```html
<!DOCTYPE html>
<html lang="en">
<head>
<meta charset="utf-8">
<title>Marwick Creations — Customized for your special needs</title>
<link href="https://fonts.googleapis.com/css2?family=Poppins:ital,wght@0,300;0,400;0,500;0,600;1,400&display=swap" rel="stylesheet">
<style>
:root{
  --gold:#c58f2f;
  --gold-dark:#b07e24;
  --ink:#1c1c1c;
  --text:#555;
  --muted:#777;
  --blue:#2a7be4;
  --soft:#f5f5f5;
  --navy:#27264a;
  --footer:#1d1d22;
  --white:#fff;
}
*{box-sizing:border-box;margin:0;padding:0}
html,body{width:1200px;height:3743px;overflow:hidden;background:var(--white)}
body{font-family:"Poppins",sans-serif;color:var(--text)}
.page{position:relative;width:1200px;height:3743px;overflow:hidden}
.abs{position:absolute}
.center{left:0;width:1200px;text-align:center}

/* header */
.brand{position:absolute;left:136px;top:22px;font-size:30px;font-weight:600;color:var(--gold);letter-spacing:1px}
.nav{position:absolute;top:31px;left:671px;display:flex;gap:0;font-size:13px;font-weight:500;color:var(--white)}
.nav a{position:absolute;white-space:nowrap;color:var(--white);text-decoration:none}
.caret{display:inline-block;margin-left:6px;border:4px solid transparent;border-top-color:var(--white);vertical-align:-1px}

/* hero */
.hero-shape{position:absolute;left:0;top:0}
.hero-tag{left:142px;top:186px;font-size:13px;font-style:italic;color:var(--text)}
.hero-title{left:142px;top:208px;font-size:50px;line-height:56px;font-weight:300;color:var(--ink)}
.hero-title strong{font-weight:600;display:block}
.hero-text{left:142px;top:343px;width:500px;font-size:13.5px;line-height:21px;color:var(--text)}
.btn{position:absolute;height:42px;border-radius:5px;font-size:13px;font-weight:500;display:flex;align-items:center;justify-content:center;background:var(--white)}
.btn-gold{border:2px solid var(--gold);color:var(--gold)}
.btn-blue{border:2px solid var(--blue);color:var(--blue)}
.ph{position:absolute}

/* section titles */
.sec-title{font-size:33px;font-weight:500;color:var(--ink)}
.rule{position:absolute;left:572px;width:56px;height:3px;background:var(--gold)}
.sec-text{font-size:12px;line-height:20px;color:var(--text)}

/* service cards */
.svc{position:absolute;top:844px;width:288px;height:388px;background:var(--white);border-radius:14px;box-shadow:0 4px 14px rgba(0,0,0,.09);border-bottom:3px solid var(--gold);overflow:hidden}
.svc .img{position:absolute;left:6px;top:6px;right:6px;height:314px;border-radius:10px}
.svc .label{position:absolute;left:20px;top:346px;font-size:16px;font-weight:500;color:var(--gold)}

/* featured */
.band-soft{position:absolute;left:0;top:1315px;width:1200px;height:620px;background:var(--soft)}
.arrow{position:absolute;width:30px;height:30px;background:var(--gold);border-radius:4px;box-shadow:0 3px 8px rgba(197,143,47,.45);display:flex;align-items:center;justify-content:center}
.prod{position:absolute;top:1545px;width:224px;height:308px;background:var(--white);border-bottom:3px solid var(--gold)}
.prod .img{position:absolute;left:42px;top:18px;width:140px;height:170px;border-radius:8px}
.prod .name{position:absolute;left:10px;right:10px;top:214px;text-align:center;font-size:16px;line-height:20px;font-weight:500;color:var(--ink)}
.prod .price{position:absolute;left:0;right:0;top:268px;text-align:center;font-size:16px;font-weight:500;color:var(--gold)}
.prod.hover .img,.prod.hover .name,.prod.hover .price{opacity:.45}
.mini{position:absolute;left:52px;width:120px;height:38px;background:rgba(255,255,255,.85);border-radius:4px;font-size:12px;display:flex;align-items:center;justify-content:center}
.mini.blue{border:2px solid var(--blue);color:var(--blue);top:105px}
.mini.gold{border:2px solid var(--gold);color:var(--gold);top:160px}

/* testimonial */
.quote-text{left:335px;top:2150px;width:530px;text-align:center;font-size:12px;line-height:20px;color:var(--text)}
.person-name{font-size:13px;font-weight:500;color:var(--ink)}
.person-role{font-size:11px;font-weight:500;color:#444}

/* appointment */
.appoint{position:absolute;left:0;top:2447px;width:1200px;height:314px;background:var(--navy)}
.appoint h2{position:absolute;left:142px;top:82px;font-size:34px;line-height:44px;font-weight:600;color:var(--white)}
.appoint p{position:absolute;left:142px;top:184px;width:310px;font-size:12px;line-height:20px;color:var(--white)}

/* contact */
.field{position:absolute;background:#fbfaf9;box-shadow:0 2px 6px rgba(0,0,0,.1);font-size:12px;color:#999;padding:12px 14px}
.send{position:absolute;left:516px;top:3188px;width:165px;height:46px;background:var(--gold);border-radius:4px;color:var(--white);font-size:13px;font-weight:500;display:flex;align-items:center;justify-content:center;gap:12px}

/* footer */
.footer{position:absolute;left:0;top:3319px;width:1200px;height:424px;background:var(--footer)}
.footer .brand{left:142px;top:112px}
.foot-about{position:absolute;left:142px;top:176px;width:175px;font-size:12px;line-height:19px;color:#eee}
.social{position:absolute;top:244px;width:32px;height:32px;border-radius:50%}
.col-title{position:absolute;top:83px;font-size:16px;font-weight:500;color:var(--gold)}
.col-link{position:absolute;font-size:12px;color:#eee}
.info{position:absolute;left:844px;font-size:12px;color:#eee;display:flex;align-items:center;gap:12px}
.subscribe{position:absolute;left:846px;top:188px;width:197px;height:47px;background:var(--white);border-radius:4px;overflow:hidden}
.subscribe span{position:absolute;left:20px;top:15px;font-size:12px;color:#999}
.subscribe i{position:absolute;right:0;top:0;width:48px;height:47px;background:var(--gold);display:flex;align-items:center;justify-content:center}
.copyright{position:absolute;left:142px;top:387px;font-size:12px;color:#eee}
</style>
</head>
<body>
<div class="page">

  <!-- hero -->
  <svg class="hero-shape" width="1200" height="620" viewBox="0 0 1200 620" aria-hidden="true">
    <path d="M411 0 H1200 V440 L905 580 Q850 620 810 585 Q790 568 780 548 Z" fill="#c58f2f"/>
  </svg>

  <div class="brand">Marwick</div>
  <nav class="nav">
    <a style="left:0">Home</a>
    <a style="left:67px">Shop<span class="caret"></span></a>
    <a style="left:144px">Services<span class="caret"></span></a>
    <a style="left:240px">Gallery</a>
    <a style="left:313px">Contact</a>
  </nav>

  <p class="abs hero-tag">Get It Customized, Get It Personalized!</p>
  <h1 class="abs hero-title">Customized for <strong>your special needs.</strong></h1>
  <p class="abs hero-text">Sed ut perspiciatis unde omnis iste natus error sit voluptatem accusantium doloremque laudantium, totam rem aperiam, eaque ipsa quae ab illo inventore veritatis et quasi architecto beatae vitae dicta sunt explicabo.</p>
  <a class="btn btn-gold" style="left:143px;top:430px;width:117px">Get a Quote</a>
  <a class="btn btn-blue" style="left:269px;top:430px;width:112px">Learn More</a>
  <div class="ph" role="img" aria-label="Desktop CNC engraving machine carving a design into a wood panel" style="left:690px;top:170px;width:365px;height:315px;border-radius:10px;background:linear-gradient(135deg,#2b2b2e 0%,#6b6b70 45%,#d9b27a 75%,#3a3a3d 100%)"></div>

  <!-- services -->
  <h2 class="abs center sec-title" style="top:676px">We Provide Custom Solutions</h2>
  <div class="rule" style="top:728px"></div>
  <p class="abs sec-text" style="left:340px;width:520px;top:739px;text-align:center">Lorem ipsum dolor sit amet, consectetur adipisicing elit. Laborum obcaecati dignissimos quae quo ad iste ipsum officiis deleniti asperiores sit.</p>

  <div class="svc" style="left:142px">
    <div class="img" role="img" aria-label="Personalized leather tags, printed mugs and an engraved tumbler" style="background:linear-gradient(160deg,#7e8f7a,#d07a45 40%,#e7c34a 60%,#3e5fa8)"></div>
    <div class="label">Home Decor &amp; Gifts</div>
  </div>
  <div class="svc" style="left:455px">
    <div class="img" role="img" aria-label="Silver horse pendant necklace and a laser cut metal panel" style="background:linear-gradient(160deg,#f4f4f4,#b8b8b8 55%,#6d6d6d)"></div>
    <div class="label">Metal Jewelry &amp; Engraving</div>
  </div>
  <div class="svc" style="left:767px">
    <div class="img" role="img" aria-label="Engraved wooden signs and name plaques" style="background:linear-gradient(160deg,#9aa0a6,#8a3c3c 40%,#a86e3e 75%,#6b4524)"></div>
    <div class="label">Engraved Wood Items</div>
  </div>

  <!-- featured collection -->
  <div class="band-soft"></div>
  <h2 class="abs center sec-title" style="top:1397px">Featured Collection</h2>
  <p class="abs center sec-text" style="top:1460px">Personalized accessories and jewelry for any style!</p>
  <div class="arrow" style="left:565px;top:1502px"><svg width="12" height="12" viewBox="0 0 12 12"><path d="M11 6H2M5 2L1 6l4 4" stroke="#fff" stroke-width="1.8" fill="none"/></svg></div>
  <div class="arrow" style="left:602px;top:1502px"><svg width="12" height="12" viewBox="0 0 12 12"><path d="M1 6h9M7 2l4 4-4 4" stroke="#fff" stroke-width="1.8" fill="none"/></svg></div>

  <div class="prod" style="left:129px">
    <div class="img" role="img" aria-label="Laser cut wooden drop earrings" style="background:linear-gradient(160deg,#f7efe5,#b8794a 55%,#4a2f22)"></div>
    <div class="name">Laser Cut Wood Earrings</div>
    <div class="price">$18.00</div>
  </div>
  <div class="prod" style="left:368px">
    <div class="img" role="img" aria-label="Stack of colourful personalized printed mugs" style="background:linear-gradient(160deg,#f3f3f3,#d9d9d9 45%,#3e64b8 70%,#e0b43a)"></div>
    <div class="name">Personalized Printed Mug</div>
    <div class="price">$12.00</div>
  </div>
  <div class="prod hover" style="left:606px">
    <div class="img" role="img" aria-label="Laser engraved metal sheet" style="background:linear-gradient(160deg,#eef2f7,#aab8cc 55%,#7a8aa3)"></div>
    <div class="name">Laser Engraved Metal Sheet</div>
    <div class="price">$19.00</div>
    <div class="mini blue">View Details</div>
    <div class="mini gold">Order Now</div>
  </div>
  <div class="prod" style="left:844px">
    <div class="img" role="img" aria-label="Personalized black and canvas market tote bags" style="background:linear-gradient(120deg,#1f1f1f 0%,#2d2d2d 45%,#eee6d4 55%,#e8ddc6 100%)"></div>
    <div class="name">Personalized Market Tote Bag</div>
    <div class="price">$22.00</div>
  </div>

  <!-- testimonial -->
  <h2 class="abs center sec-title" style="top:2018px">Our Customers Trust Us</h2>
  <div class="rule" style="top:2070px"></div>
  <svg class="abs" style="left:338px;top:2126px" width="28" height="22" viewBox="0 0 28 22" aria-hidden="true">
    <path d="M0 22V12C0 5 4 1 10 0l1 3C7 4 5 7 5 10h6v12zM16 22V12c0-7 4-11 10-12l1 3c-4 1-6 4-6 7h6v12z" fill="#222"/>
  </svg>
  <p class="abs quote-text">Lorem ipsum dolor sit amet, consectetur adipisicing elit. A impedit, quas. Ad minus voluptatibus corporis eaque deleniti, quam, voluptates quidem similique tenetur reiciendis libero atque hic expedita officia provident perferendis.</p>
  <div class="ph" role="img" aria-label="Customer portrait" style="left:570px;top:2232px;width:60px;height:60px;border-radius:50%;background:linear-gradient(180deg,#d9d9d9,#8e8e8e)"></div>
  <p class="abs center person-name" style="top:2306px">Daniel Reyes</p>
  <p class="abs center person-role" style="top:2328px">Director, Harlow &amp; Pine Inc.</p>
  <div class="arrow" style="left:565px;top:2371px"><svg width="12" height="12" viewBox="0 0 12 12"><path d="M11 6H2M5 2L1 6l4 4" stroke="#fff" stroke-width="1.8" fill="none"/></svg></div>
  <div class="arrow" style="left:602px;top:2371px"><svg width="12" height="12" viewBox="0 0 12 12"><path d="M1 6h9M7 2l4 4-4 4" stroke="#fff" stroke-width="1.8" fill="none"/></svg></div>

  <!-- appointment -->
  <section class="appoint">
    <h2>Schedule an<br>Appointment</h2>
    <p>Please use the contact form below to schedule an appointment to discuss your project.</p>
    <div class="ph" role="img" aria-label="Collection of engraved wooden signs, plaques and keepsakes" style="left:549px;top:24px;width:602px;height:218px;background:linear-gradient(120deg,#c7a06c,#e2c79b 45%,#b98a55 70%,#e6e3dd)"></div>
  </section>

  <!-- contact -->
  <h2 class="abs center sec-title" style="top:2844px">Get In Touch</h2>
  <div class="rule" style="top:2896px"></div>
  <p class="abs sec-text" style="left:370px;width:460px;top:2906px;text-align:center">Lorem ipsum dolor sit amet, consectetur adipisicing elit. Laborum obcaecati dignissimos quae quo ad iste ipsum officiis deleniti asperiores sit.</p>
  <div class="field" style="left:221px;top:3013px;width:366px;height:38px">Name</div>
  <div class="field" style="left:221px;top:3067px;width:366px;height:38px">Email</div>
  <div class="field" style="left:221px;top:3121px;width:366px;height:38px">Subject</div>
  <div class="field" style="left:610px;top:3013px;width:366px;height:146px">Message</div>
  <div class="send">
    <svg width="13" height="13" viewBox="0 0 14 14" aria-hidden="true"><path d="M13 1L1 6l5 2 2 5z" fill="#fff"/></svg>
    Send Message
  </div>

  <!-- footer -->
  <footer class="footer">
    <div class="brand">Marwick</div>
    <p class="foot-about">Lorem ipsum dolor sit amet, consectetur adipisicing elit laboriosam vitae.</p>
    <span class="social" style="left:147px;background:#3b5bb5"></span>
    <span class="social" style="left:187px;background:#2aa3e8"></span>
    <span class="social" style="left:228px;background:#d9423a"></span>
    <span class="social" style="left:270px;background:#1fb37a"></span>

    <h3 class="col-title" style="left:376px">Company</h3>
    <span class="col-link" style="left:376px;top:117px">About Us</span>
    <span class="col-link" style="left:376px;top:150px">Our Services</span>
    <span class="col-link" style="left:376px;top:182px">Career</span>
    <span class="col-link" style="left:376px;top:215px">Read our Blog</span>

    <h3 class="col-title" style="left:610px">Support</h3>
    <span class="col-link" style="left:610px;top:117px">Legal Information</span>
    <span class="col-link" style="left:610px;top:150px">Privacy Policy</span>
    <span class="col-link" style="left:610px;top:182px">Terms &amp; Conditions</span>
    <span class="col-link" style="left:610px;top:215px">Report Abuse</span>

    <h3 class="col-title" style="left:844px">Get in touch</h3>
    <div class="info" style="top:117px">
      <svg width="13" height="12" viewBox="0 0 13 12" aria-hidden="true"><path d="M6.5 0L0 5.5h2V12h3.5V8h2v4H11V5.5h2z" fill="#eee"/></svg>
      418 Orchard Ln, Millbrook, NY 12545
    </div>
    <div class="info" style="top:150px">
      <svg width="12" height="12" viewBox="0 0 12 12" aria-hidden="true"><path d="M2.5 0L4.5 3 3.3 4.4c.7 1.6 2.2 3.1 3.8 3.8L8.5 7 12 9l-1 2.5C5 12 0 7 .5 1z" fill="#eee"/></svg>
      +1 555-014-2290
    </div>
    <div class="subscribe">
      <span>Enter Email</span>
      <i><svg width="13" height="13" viewBox="0 0 14 14" aria-hidden="true"><path d="M13 1L1 6l5 2 2 5z" fill="#fff"/></svg></i>
    </div>
    <p class="copyright">© Copyrights 2023 Marwick Creations LLC. All rights reserved.</p>
  </footer>
</div>
</body>
</html>
```